Web page design - online proposal

We have an feature in our CRM to produce online proposals but at the moment they look very boring and plain. We need fresh new exciting designs for them that look highly professional.
We will be choosing 5 designs to use as templates so our users can upload their logo, photos and select their colours so that it generates a professional looking proposal for them.

Here is a sample of one of the existing proposals. All the information that's in the proposal will be used:

https://www.corvellahomes.com.au/portal/proposal.aspx?id=2837&passcode=KRMWPL42&preview=1

One suggestion is to include compelling background images of houses. Also need to show a proposal date at the start of the document along with something that says 'This proposal is valid for 30 days'

```html
<!DOCTYPE html>
<html lang="en">
<head>
<meta charset="utf-8">
<title>Proposal for Residential Property Development</title>
<link href="https://fonts.googleapis.com/css2?family=Inter:wght@400;500;600;700&family=Source+Serif+4:wght@400;500;600&display=swap" rel="stylesheet">
<style>
  :root {
    --navy: #15233a;
    --gold: #e6c36a;
    --gold-band: #b8964e;
    --paper: #fbf9f5;
    --ink: #1a2233;
    --white: #ffffff;
  }
  * { margin: 0; padding: 0; box-sizing: border-box; }
  html, body { width: 800px; height: 1200px; overflow: hidden; }
  body { background: var(--paper); font-family: "Inter", sans-serif; color: var(--ink); }
  .proposal { position: relative; width: 800px; height: 1200px; background: var(--paper); }
  .masthead { position: absolute; left: 0; top: 0; width: 800px; height: 377px; background: var(--navy); }
  .brand-name { position: absolute; left: 66px; top: 88px; font-family: "Inter", sans-serif; font-size: 24px; font-weight: 600; line-height: 1; color: var(--gold); letter-spacing: 0.5px; }
  .title { position: absolute; left: 66px; top: 158px; font-family: "Source Serif 4", serif; font-weight: 500; font-size: 51px; line-height: 59px; color: var(--white); letter-spacing: -0.3px; }
  .dateline { position: absolute; left: 66px; top: 292px; font-size: 19px; color: var(--gold); display: flex; gap: 18px; align-items: center; }
  .dateline strong { font-weight: 600; }
  .dateline .sep { width: 1px; height: 16px; background: var(--gold); opacity: .7; }
  .photo { position: absolute; }
  .photo-hero { left: 352px; top: 347px; width: 448px; height: 303px; background: linear-gradient(180deg, #c9cdd2 0%, #e6d9c8 35%, #f0eeea 55%, #8f9a86 82%, #5f7a45 100%); }
  .photo-second { left: 372px; top: 802px; width: 362px; height: 188px; background: linear-gradient(180deg, #b7c6d6 0%, #dde3e6 40%, #c9a47a 62%, #6f8a4c 100%); }
  .label { position: absolute; font-size: 18.5px; font-weight: 600; letter-spacing: 1.4px; color: var(--ink); }
  .value { position: absolute; font-size: 20px; line-height: 29px; color: var(--ink); }
  .subhead { position: absolute; font-size: 18.5px; color: var(--ink); letter-spacing: .3px; }
  .copy { position: absolute; font-size: 14.5px; line-height: 23.5px; color: var(--ink); }
  .serif-head { position: absolute; font-family: "Source Serif 4", serif; font-size: 20px; color: var(--ink); }
  .pricing { position: absolute; left: 66px; top: 916px; width: 263px; height: 207px; background: var(--navy); }
  .pricing-head { height: 51px; background: var(--gold-band); color: var(--white); font-weight: 700; font-size: 18px; letter-spacing: 1px; padding: 15px 22px 0; }
  .pricing-row { display: flex; justify-content: space-between; color: var(--white); font-size: 15px; padding: 0 17px 0 22px; height: 31.5px; align-items: center; }
  .pricing-row.first { margin-top: 12px; }
  .pricing-rule { margin: 6px 12px 0 17px; height: 2px; background: var(--gold-band); }
  .pricing-total { display: flex; justify-content: space-between; color: var(--white); font-size: 16px; padding: 11px 15px 0 22px; letter-spacing: .5px; }
  .pricing-total strong { font-weight: 700; font-size: 17px; }
  .footer { position: absolute; left: 0; top: 1140px; width: 800px; height: 60px; background: var(--navy); color: var(--white); font-size: 16.5px; display: flex; align-items: center; justify-content: center; gap: 20px; padding-left: 40px; }
  .footer .sep { width: 1px; height: 15px; background: var(--white); opacity: .6; }
</style>
</head>
<body>
<main class="proposal">
  <header class="masthead">
    <div class="brand-name">Northway Real Estate</div>
    <h1 class="title">Proposal for Residential<br>Property Development</h1>
    <div class="dateline"><strong>April 30, 2024</strong><span class="sep"></span><span>Valid for 30 days</span></div>
  </header>

  <div class="photo photo-hero" role="img" aria-label="Photo of a white two-storey house with a dark roof, lit windows and a wooden garage door at dusk"></div>

  <div class="label" style="left:66px; top:419px;">CLIENT NAME</div>
  <div class="value" style="left:66px; top:447px;">John Doe</div>

  <div class="label" style="left:66px; top:500px;">PROJECT TITLE</div>
  <div class="value" style="left:66px; top:529px;">Proposed Residential<br>Development</div>

  <div class="subhead" style="left:66px; top:617px;">Introduction or summary</div>
  <p class="copy" style="left:66px; top:652px; width:250px;">Cerlus et dolor im rostu main ar. consenos in apestindoto nunco amet ram aquiplang esi lings viteri unes. Cuni udes slate taq nteestean cagunuit.</p>

  <div class="label" style="left:66px; top:803px;">PROJECT SCOPE</div>
  <p class="copy" style="left:66px; top:838px; width:250px;">Etcer po filericam sonru ars orepium catur co, tenotivos saptiesir</p>

  <section class="pricing">
    <div class="pricing-head">PRICING</div>
    <div class="pricing-row first"><span>Planning and Design</span><span>$3,000</span></div>
    <div class="pricing-row"><span>Construction</span><span>$278,000</span></div>
    <div class="pricing-row"><span>Landscaping</span><span>$25,000</span></div>
    <div class="pricing-rule"></div>
    <div class="pricing-total"><span>TOTAL</span><strong>$305,000</strong></div>
  </section>

  <div class="label" style="left:372px; top:679px;">PROJECT OVERVIEW</div>
  <p class="copy" style="left:372px; top:714px; width:366px;">Lorem ipsum dolor sit amet, consectetur adipsicing elit, sed do elusmod tempor incididunt ut labore et dolore magna aliqua.</p>

  <div class="photo photo-second" role="img" aria-label="Photo of a single-storey house with timber cladding and large lit windows on a green lawn"></div>

  <div class="serif-head" style="left:372px; top:1016px;">Dimenssergation</div>
  <p class="copy" style="left:372px; top:1052px; width:370px;">Citam reas maire drum sit inso internanes cen aule ines achuus asquem ocaute quam</p>

  <footer class="footer">
    <span>(555) 318-2046</span><span class="sep"></span><span>info@northwayrealestate.com</span><span>www.northwayrealestate.com</span>
  </footer>
</main>
</body>
</html>
```